Healthy juice company needs a branded shipping box

I am looking for a branded box that is 10"x10"x10" in standard brown. This is for the box we ship the juice in.

The box should serve as an advertising platform in itself. We offer a subscription juice service. People get a box of juice delivered every week.

The customer should see the box and feel good about what they ordered because it's something healthy they're doing for themselves. The imagery/wording should reinforce that they're doing something healthy for themselves.

Other people who see the box should be curious enough to look us up and want a box for themselves.

I'd like ONE color in the final print.

I'd like the 4 sides of the box to be printed.

The design is up to you.

Inspiration boxes: Amber Ladle, Tidy Basket, PrintHollow

Target Market(s)

Our customers subscribe to our juice because it helps them eat the fruits and veggies they normally wouldn't. They are typically 30-40yrs old, with families, and are upper middle class.

Industry/Entity Type

Delivery Service

Font styles to use
Sans Serif

Colors
f78f20
9bcb3c
ffffff

Requirements
Must have
• The design should feel clean, bright, happy, casual, and healthy.
• Natural fruits & veggies are part of what we do.
• Has to convey farm fresh, fresh made and locally made through the design.
• Must have website: www.varolipressery.example
Nice to have
• These can optionally be included on the box:
• - "I care about my health."
• - "Drink Juice. Live Healthier."
• The box can be branded "The Pulp Crate" on 1+ sides

```html
<!DOCTYPE html>
<html lang="en">
<head>
<meta charset="utf-8">
<title>Varoli Pressery – Shipping Box Dieline</title>
<link href="https://fonts.googleapis.com/css2?family=Fira+Sans:wght@300;400&family=Fira+Sans+Condensed:wght@400;700&display=swap" rel="stylesheet">
<style>
  :root {
    --ink: #169c48;
    --ink-soft: #5cbf7f;
    --paper: #ffffff;
    --canvas: #ffffff;
  }
  * { margin: 0; padding: 0; box-sizing: border-box; }
  html, body {
    width: 1200px; height: 900px; overflow: hidden;
    background: var(--canvas);
  }
  .sheet { position: relative; width: 1200px; height: 900px; }
  .brand-lockup {
    position: absolute; left: 48px; top: 262px;
    font-family: "Fira Sans", sans-serif; font-weight: 300;
    font-size: 52px; color: var(--ink); letter-spacing: 1px;
  }
  .dieline { position: absolute; left: 20px; top: 370px; }
  .ink { fill: var(--ink); }
  .ink-soft { fill: var(--ink-soft); }
  .light-copy { font-family: "Fira Sans", sans-serif; font-weight: 300; fill: var(--paper); }
  .bold-copy { font-family: "Fira Sans Condensed", sans-serif; font-weight: 700; fill: var(--paper); font-variant: small-caps; }
  .url { font-family: "Fira Sans Condensed", sans-serif; font-weight: 700; fill: var(--paper); font-size: 11px; letter-spacing: .3px; }
  .panel-brand { font-family: "Fira Sans", sans-serif; font-weight: 300; fill: var(--paper); }
  .icon { fill: none; stroke: var(--paper); stroke-width: 1.8; }
  .fold { stroke: var(--paper); stroke-width: 2; }
</style>
</head>
<body>
<div class="sheet">
  <div class="brand-lockup">Varoli Pressery</div>

  <svg class="dieline" width="1160" height="290" viewBox="0 0 1160 290">
    <!-- Panel 1: The Pulp Crate -->
    <g class="panel panel-crate">
      <path class="ink" d="M0,225 C25,235 40,255 45,282 C95,200 190,150 290,145 L290,290 L0,290 Z"/>
      <text class="light-copy" x="280" y="248" font-size="21" text-anchor="end" letter-spacing="1" style="font-variant:small-caps">The Pulp Crate</text>
      <text class="url" x="280" y="274" text-anchor="end">WWW.VAROLIPRESSERY.EXAMPLE</text>
    </g>

    <!-- Panel 2: promise copy -->
    <g class="panel panel-promise" transform="translate(290,0)">
      <path class="ink" d="M0,290 L0,160 C22,150 42,138 52,112 C72,40 130,0 230,0 L290,0 L290,290 Z"/>
      <text class="light-copy" x="283" y="32" font-size="16" text-anchor="end">Locally prepared with</text>
      <text class="bold-copy" x="283" y="63" font-size="29" text-anchor="end">All-Natural</text>
      <text class="light-copy" x="283" y="86" font-size="16" text-anchor="end">Fruits and Vegetables</text>
      <text class="bold-copy" x="283" y="117" font-size="29" text-anchor="end">Fresh</text>
      <text class="light-copy" x="283" y="138" font-size="16" text-anchor="end">from the farm</text>
      <rect class="ink-soft" x="20" y="185" width="95" height="105" role="img" aria-label="Leaf sprout illustration"/>
    </g>

    <!-- Panel 3: brand and juice glass -->
    <g class="panel panel-brandside" transform="translate(580,0)">
      <rect class="ink" x="0" y="0" width="290" height="290"/>
      <text class="panel-brand" font-size="56" text-anchor="middle" transform="translate(82,112) rotate(-90)">Varoli</text>
      <text class="panel-brand" x="62" y="228" font-size="22" text-anchor="middle">Pressery</text>
      <text class="url" x="6" y="274">WWW.VAROLIPRESSERY.EXAMPLE</text>
      <rect class="ink-soft" x="160" y="0" width="125" height="255" role="img" aria-label="Juice glass with fruit splash illustration"/>
    </g>

    <!-- Panel 4: benefits list -->
    <g class="panel panel-benefits" transform="translate(870,0)">
      <path class="ink" d="M0,0 L200,0 C235,60 265,140 290,200 L290,290 L0,290 Z"/>
      <text class="panel-brand" x="18" y="38" font-size="22">Varoli Pressery</text>
      <g class="benefit">
        <circle class="icon" cx="28" cy="94" r="11"/>
        <text class="bold-copy" x="50" y="99" font-size="16">Raw Juice</text>
      </g>
      <g class="benefit">
        <circle class="icon" cx="28" cy="134" r="11"/>
        <text class="bold-copy" x="50" y="139" font-size="16">Never Heated</text>
      </g>
      <g class="benefit">
        <circle class="icon" cx="28" cy="174" r="11"/>
        <text class="bold-copy" x="50" y="179" font-size="16">Locally Sourced</text>
      </g>
      <g class="benefit">
        <circle class="icon" cx="28" cy="216" r="11"/>
        <text class="bold-copy" x="50" y="221" font-size="16">Cold Pressed</text>
      </g>
      <g class="benefit">
        <circle class="icon" cx="28" cy="256" r="11"/>
        <text class="bold-copy" x="50" y="261" font-size="16">Gluten Free</text>
      </g>
    </g>

    <!-- fold lines between panels -->
    <line class="fold" x1="290" y1="150" x2="290" y2="290"/>
    <line class="fold" x1="580" y1="0" x2="580" y2="290"/>
    <line class="fold" x1="870" y1="0" x2="870" y2="290"/>
  </svg>
</div>
</body>
</html>
```